CrestHornSupply.com

I need a new webdesign for a company in the San Jose/SF Bay area that showcases the financial benefits of buying used band instruments for junior high students.This would be opposed to the current and costly option of renting cheap quality instruments from the 2 or 3 local music stores that charge a monthly fee that over the years charges the buyer 3 or 4x over..
Instruments: focus in on Alto Sax, Trumpet, Flute, Clarinet, Trombone, Tenor Sax, Baritone
Target middle schools are Willowmere Middle School and Harlan Middle School in San Jose, CA. Both have award winning band programs.
Files attached may or may not be important.
Tabs Needed and funtional
Contact
Shopping Cart
Select Instrument
Checkout
Add to Cart, etc.
Instuments
quantity, etc.
trade in your instrument/sell your instrument
ability to add or take away new instruments for sale. including pictures
Additional questions or info, feel free to ask
Updates
Hi Designers,
Project Deadline Extended
Reason: In the next week you will be receiving specific content that will be required to be had on the website.
New desigins are still welcome. Please continue to contact me if you have questions about your individual designs.
Thanks!
Crest Horn

```html
<!DOCTYPE html>
<html lang="en">
<head>
<meta charset="utf-8">
<title>Crest Horn Supply</title>
<link href="https://fonts.googleapis.com/css2?family=Open+Sans:wght@400;600;700&display=swap" rel="stylesheet">
<style>
:root{
  --red:#b90f14;
  --blue:#0a84d6;
  --dark:#555555;
  --darker:#333333;
  --footer:#404040;
  --text:#444444;
  --line:#dddddd;
  --bg:#f3f3f3;
  --white:#ffffff;
}
*{box-sizing:border-box;margin:0;padding:0}
html,body{width:1036px;height:1200px;overflow:hidden}
body{font-family:"Open Sans",sans-serif;color:var(--text);background:var(--bg);font-size:11px;position:relative}
.wrap{width:847px;margin:0 auto;position:relative}
a{color:inherit;text-decoration:none}

.topbar{height:26px;background:var(--dark);color:var(--white);font-size:9px}
.topbar .wrap{display:flex;justify-content:space-between;align-items:center;height:26px}
.topbar nav{display:flex}
.topbar nav a{padding:0 9px;border-left:1px solid #6a6a6a;line-height:26px}
.topbar nav a:first-child{border-left:0}
.topbar nav a:last-child{padding-right:0}

.header{height:91px;background:var(--white)}
.header .wrap{height:91px}
.brand{position:absolute;left:0;top:35px;font-size:21px;font-weight:600;color:var(--red)}
.phone{position:absolute;right:0;top:12px;font-size:20px;font-weight:600;color:#9a9a9a}
.search{position:absolute;left:452px;top:52px;display:flex}
.search .field{width:203px;height:25px;border:1px solid var(--line);font-size:11px;color:#666;padding:5px 9px}
.search .btn{width:28px;height:25px;background:var(--blue);display:flex;align-items:center;justify-content:center}
.cart{position:absolute;right:0;top:58px;display:flex;align-items:center;gap:4px;font-size:11px;color:#111}
.cart .price{color:var(--red)}
.cart .checkout{color:var(--blue);margin-left:4px}

.mainnav{height:34px;background:var(--red)}
.mainnav .wrap{display:flex;height:34px}
.mainnav a{color:var(--white);font-size:11.5px;font-weight:600;line-height:34px;padding:0 9px;border-left:1px solid #d8494d;letter-spacing:-.2px}
.mainnav a:first-child{border-left:0;padding-left:1px}

.hero{height:338px;background:linear-gradient(#ededed,#f7f7f7 70%,#e8e8e8)}
.hero .wrap{height:338px}
.hero h1{position:absolute;left:0;top:100px;font-size:27px;font-weight:700;color:var(--darker);letter-spacing:-.5px}
.hero p{position:absolute;left:0;top:141px;width:370px;font-size:12px;line-height:17.5px;color:#555}
.btn-blue{display:inline-block;background:var(--blue);color:var(--white);border-radius:2px;font-size:12px;text-align:center}
.hero .btn-blue{position:absolute;left:2px;top:207px;width:77px;height:23px;line-height:23px}
.dots{position:absolute;left:1px;top:298px;display:flex;gap:5px}
.dots i{width:11px;height:11px;border-radius:50%;background:#777}
.dots i:first-child{background:#222}
.hero-art{position:absolute;right:0;top:36px;width:365px;height:270px;border-radius:50%/45%;background:radial-gradient(ellipse at 55% 50%,#e8c25a,#cf9c2e 40%,rgba(240,240,240,0) 72%)}

.features{display:flex;gap:10px;margin-top:8px}
.feature{width:204px;height:94px;background:var(--white);border:1px solid var(--line);position:relative}
.feature .ico{position:absolute;left:15px;top:13px;width:67px;height:67px;border-radius:50%;border:2px solid #ddd;display:flex;align-items:center;justify-content:center}
.feature .txt{position:absolute;right:17px;top:20px;text-align:right}
.feature b{display:block;font-size:20px;font-weight:700;color:#444;line-height:24px}
.feature small{font-size:12px;color:#666}

.section-title{text-align:center;font-size:21px;font-weight:400;color:#333;margin:24px 0 14px}

.products{display:flex;gap:10px}
.product{width:204px;height:193px;background:var(--white);border:1px solid var(--line);position:relative;overflow:hidden;text-align:center}
.product .shot{width:140px;height:100px;margin:20px auto 0;border-radius:50%;background:radial-gradient(ellipse,#d9b25a,rgba(255,255,255,0) 70%)}
.product .shot.wood{background:radial-gradient(ellipse,#c98e4e,rgba(255,255,255,0) 65%)}
.product .shot.black{background:radial-gradient(ellipse,#333,rgba(255,255,255,0) 65%)}
.product .name{margin-top:10px;font-size:12px;color:#333}
.product .name em{font-style:normal;color:var(--red);font-weight:600;margin-left:6px}
.product .btn-blue{width:77px;height:23px;line-height:23px;margin-top:11px}
.ribbon{position:absolute;left:-28px;top:16px;width:120px;height:22px;background:var(--red);color:var(--white);font-size:12px;font-weight:700;line-height:22px;transform:rotate(-45deg);text-align:center}
.arrow{position:absolute;top:741px;width:24px;height:24px;border-radius:50%;background:#555;display:flex;align-items:center;justify-content:center}

.info{display:flex;height:132px;margin-top:13px;background:var(--white);border:1px solid var(--line)}
.info > div{padding:16px 24px}
.newsletter{width:403px;border-right:1px solid var(--line)}
.payment{padding-left:76px!important}
.info h2{font-size:21px;font-weight:400;color:#333;margin-bottom:5px}
.info p{font-size:10px;line-height:17px;color:#555;width:290px}
.signup{display:flex;gap:7px;margin-top:8px}
.signup .field{width:215px;height:29px;border:1px solid var(--line)}
.signup .btn-blue{width:80px;height:29px;line-height:29px;font-size:13px;border-radius:0}
.cards{display:flex;gap:13px;margin-top:9px}
.cards span{width:40px;height:25px;border:1px solid #ccc;border-radius:2px;background:#f7f7f7;font-size:7px;font-weight:600;color:#555;display:flex;align-items:center;justify-content:center}

.footer{position:absolute;top:1016px;left:0;width:1036px;height:150px;background:var(--footer)}
.footer .wrap{height:150px}
.footer h3{position:absolute;top:14px;font-size:12px;font-weight:700;color:var(--white)}
.footer ul{position:absolute;top:42px;list-style:none}
.footer li{font-size:10.5px;color:#bbb;line-height:20px}
.follow{position:absolute;left:731px;top:40px}
.follow div{display:flex;align-items:center;gap:10px;height:31px;font-size:11px;color:var(--white)}
.follow i{width:28px;height:28px;border-radius:50%;background:#ccc}
.bottombar{position:absolute;top:1166px;left:0;width:1036px;height:34px;background:var(--darker);color:#aaa;font-size:9px;text-align:center;line-height:44px}
</style>
</head>
<body>
<div class="topbar"><div class="wrap">
  <span>24x7 Customer Care</span>
  <nav><a href="#">Login</a><a href="#">Signup</a><a href="#">My Account</a><a href="#">Order Status</a><a href="#">Wish List</a></nav>
</div></div>

<header class="header"><div class="wrap">
  <div class="brand">Crest Horn Supply</div>
  <div class="phone">(800) 555-0142</div>
  <div class="search">
    <div class="field">Product Search</div>
    <div class="btn"><svg width="13" height="13" viewBox="0 0 13 13"><circle cx="5.5" cy="5.5" r="4" fill="none" stroke="#fff" stroke-width="1.8"/><line x1="8.5" y1="8.5" x2="12" y2="12" stroke="#fff" stroke-width="2"/></svg></div>
  </div>
  <div class="cart">
    <svg width="22" height="16" viewBox="0 0 22 16"><path d="M0 1h4l3 10h11l3-8H6" fill="none" stroke="#111" stroke-width="2"/><path d="M6 4h14l-2.5 6H8z" fill="#111"/><circle cx="8" cy="14" r="1.6" fill="#111"/><circle cx="17" cy="14" r="1.6" fill="#111"/></svg>
    <span>0Items <span class="price">($0.00)</span></span><a class="checkout" href="#">Checkout</a>
  </div>
</div></header>

<nav class="mainnav"><div class="wrap">
  <a href="#">HOME</a><a href="#">ABOUT US</a><a href="#">PRODUCTS</a><a href="#">SALE</a><a href="#">SELECT INSTRUMENT</a><a href="#">INSTUMENTS</a><a href="#">QUANTITY</a><a href="#">CONTACT US</a>
</div></nav>

<section class="hero"><div class="wrap">
  <h1>BAND INSTRUMENTS</h1>
  <p>Lorem Ipsum is simply dummy text of the printing and typesetting industry. Lorem Ipsum has been the industry's standard dummy text ever since the 1500s</p>
  <a class="btn-blue" href="#">Buy Now</a>
  <div class="dots"><i></i><i></i><i></i></div>
  <div class="hero-art" role="img" aria-label="Two brass trumpets on a light background"></div>
</div></section>

<main class="wrap">
  <div class="features">
    <div class="feature">
      <div class="ico"><svg width="40" height="30" viewBox="0 0 40 30"><g transform="rotate(-30 20 15)"><path d="M4 8h26l8 7-8 7H4z" fill="#d01d22"/><circle cx="31" cy="15" r="2" fill="#fff"/><text x="16" y="19" font-size="9" font-weight="700" fill="#fff" text-anchor="middle" font-family="Open Sans,sans-serif">SALE</text></g></svg></div>
      <div class="txt"><b>Special</b><small>Discount Items</small></div>
    </div>
    <div class="feature">
      <div class="ico"><svg width="30" height="30" viewBox="0 0 24 24"><path d="M6.6 10.8a15 15 0 0 0 6.6 6.6l2.2-2.2a1 1 0 0 1 1-.25 11 11 0 0 0 3.6.6 1 1 0 0 1 1 1V20a1 1 0 0 1-1 1A17 17 0 0 1 3 4a1 1 0 0 1 1-1h3.5a1 1 0 0 1 1 1c0 1.25.2 2.45.6 3.6a1 1 0 0 1-.25 1z" fill="#c4161c"/></svg></div>
      <div class="txt"><b>24/7 Live</b><small>Customer Service</small></div>
    </div>
    <div class="feature">
      <div class="ico"><svg width="50" height="50"><circle cx="25" cy="25" r="25" fill="#c4161c"/></svg></div>
      <div class="txt"><b>Join Us</b><small>On Friendwall</small></div>
    </div>
    <div class="feature">
      <div class="ico"><span style="font-size:40px;font-weight:700;color:#c4161c;line-height:1">?</span></div>
      <div class="txt"><b>About us</b><small>Click Here</small></div>
    </div>
  </div>

  <h2 class="section-title">Featured Products</h2>

  <div class="products">
    <div class="product"><div class="ribbon">SALE</div><div class="shot" role="img" aria-label="Alto saxophone"></div><div class="name">Alto Sax<em>($100)</em></div><a class="btn-blue" href="#">Buy Now</a></div>
    <div class="product"><div class="shot" role="img" aria-label="Trumpet"></div><div class="name">Trumpet<em>($100)</em></div><a class="btn-blue" href="#">Buy Now</a></div>
    <div class="product"><div class="shot wood" role="img" aria-label="Wooden flute"></div><div class="name">Flute<em>($100)</em></div><a class="btn-blue" href="#">Buy Now</a></div>
    <div class="product"><div class="shot black" role="img" aria-label="Clarinet"></div><div class="name">Clarinet<em>($100)</em></div><a class="btn-blue" href="#">Buy Now</a></div>
  </div>

  <div class="info">
    <div class="newsletter">
      <h2>Newsletter SignUp</h2>
      <p>Lorem Ipsum is simply dummy text of the printing and typesetting industry.</p>
      <div class="signup"><div class="field"></div><a class="btn-blue" href="#">Subscribe</a></div>
    </div>
    <div class="payment">
      <h2>Payment Method</h2>
      <p>Lorem Ipsum is simply dummy text of the printing and typesetting industry.</p>
      <div class="cards"><span>Veltra</span><span>Meridian</span><span>Jovi</span><span>Coinwell</span><span>Dovecard</span><span>Amberline</span></div>
    </div>
  </div>
</main>

<a class="arrow" style="left:63px" href="#"><svg width="8" height="8"><path d="M6 1L2 4l4 3z" fill="#fff"/></svg></a>
<a class="arrow" style="left:948px" href="#"><svg width="8" height="8"><path d="M2 1l4 3-4 3z" fill="#fff"/></svg></a>

<footer class="footer"><div class="wrap">
  <h3 style="left:1px">Order Info</h3>
  <ul style="left:1px"><li>How to Order</li><li>My Account</li><li>Order Status</li><li>Shipping</li><li>Policies &amp; Guarantees</li></ul>
  <ul style="left:142px"><li>Warranties</li><li>Contact Us</li></ul>
  <h3 style="left:266px">Additional Info</h3>
  <ul style="left:266px"><li>Tech Support</li><li>Learning Center</li><li>Shopping Cart</li><li>Instuments</li><li>Affiliate Program</li></ul>
  <ul style="left:398px"><li>Reseller Program</li><li>Privacy Policy</li><li>Terms of Use</li><li>Sitemap</li></ul>
  <h3 style="left:557px">About Us</h3>
  <ul style="left:557px"><li>About Us</li><li>Careers</li><li>Blog</li><li>Press</li><li>Online Shopping</li></ul>
  <h3 style="left:731px">Follow Us</h3>
  <div class="follow">
    <div><i></i>Friendwall</div>
    <div><i></i>Chirper</div>
    <div><i></i>ClipStream</div>
  </div>
</div></footer>
<div class="bottombar">© 2014 CrestHornSupply.com. All Right Reserved</div>
</body>
</html>
```